Software Product Flyer Design

A established czech software company needs a marketing flyer to promote their software product and its modules.
The overall feel of the flyer must to be serious, but also eye-catching, enticing, clever and bold to attract customers.
Unifying graphic element is the new product logo.
The flyer would be A4, colour both sides and folded once (to give 4 pages of A5).
Title page - product logo with module name and module icon, short presentation of the product and list of its key features.
Inside pages - detailed informations with screenshots or graphical schemas.
Back side - informations about technical requirements and user support, contacts (address, phone, fax, e-mail, web pages - no social networks).
Product logo, module icon and some images attached.
Updates
Hello,
Reason: For organizational reasons we extending the deadline by 10 days.
FYI: We have uploaded the new ZIP file with previous version of our flyer.
Attached PDF file with text for inner pages.
Target Market(s)
Existing or new customers like municipalities, public authorities and nonprofit organizations.
Industry/Entity Type
Marketing
Requirements
Must have
- Winning designer must provide a template for Adobe InDesign based on his graphic design.
Avoid to using exotic fonts - in Czech we use Latin Extended characters (like áéěíýůčřžšťďň).
Nice to have
- Using graphic motif from product logo like as attached splash screen.

```html
<!DOCTYPE html>
<html lang="cs">
<head>
<meta charset="utf-8">
<title>Nevrisa – produktový leták</title>
<link rel="stylesheet" href="https://fonts.googleapis.com/css2?family=Open+Sans:wght@300;400;600;700&display=swap">
<style>
  :root {
    --slate: #4a4e54;
    --slate-dark: #3a3d42;
    --orange: #f26a21;
    --orange-light: #f7893f;
    --white: #ffffff;
    --ink: #4b4f55;
    --text-muted: #5c6066;
  }
  * { box-sizing: border-box; margin: 0; padding: 0; }
  html, body { width: 818px; height: 1200px; overflow: hidden; }
  body { font-family: "Open Sans", Arial, sans-serif; background: var(--slate); }

  .flyer { position: relative; width: 818px; height: 1200px; background: var(--slate); overflow: hidden; }

  .shapes { position: absolute; inset: 0; }

  .brand {
    position: absolute; left: 470px; top: 70px; width: 310px; height: 150px;
    background: var(--white); border-radius: 40px;
    display: flex; align-items: center; justify-content: center;
  }
  .brand-name { font-size: 52px; font-weight: 600; color: var(--slate); letter-spacing: 2px; line-height: 1; text-transform: uppercase; }

  .hero-photo {
    position: absolute; left: 28px; top: 300px; width: 400px; height: 450px;
    border-radius: 46px; border: 14px solid #6a6f76;
    background: radial-gradient(circle at 55% 40%, #e8f1f8 0%, #a9bccb 35%, #5c6b79 75%, #3f4650 100%);
  }

  .intro { position: absolute; left: 462px; top: 500px; width: 340px; color: var(--white); }
  .intro-title { font-size: 22px; font-weight: 400; margin-bottom: 14px; white-space: nowrap; }
  .intro-text { font-size: 13px; line-height: 1.45; font-weight: 300; }

  .features { position: absolute; left: 36px; top: 850px; width: 360px; }
  .features-title { font-size: 26px; font-weight: 400; color: var(--ink); margin-bottom: 14px; }
  .features-list { list-style: none; }
  .features-list li {
    position: relative; padding-left: 26px; font-size: 14.5px; line-height: 1.3;
    color: var(--text-muted); margin-bottom: 5px;
  }
  .features-list li::before {
    content: ""; position: absolute; left: 0; top: 5px; width: 10px; height: 10px; background: var(--orange);
  }
  .website {
    position: absolute; left: 36px; top: 1148px; font-size: 18px; letter-spacing: 4px;
    color: var(--orange); font-weight: 400;
  }

  .module-band {
    position: absolute; left: 436px; top: 870px; width: 382px; height: 64px;
    background: var(--white); display: flex; align-items: center; padding-left: 34px;
  }
  .module-name { font-size: 34px; letter-spacing: 7px; color: var(--slate-dark); font-weight: 400; }
  .module-icon {
    position: absolute; left: 520px; top: 975px; width: 220px; height: 190px; border-radius: 10px;
    background: linear-gradient(135deg, #f5f2ea 0%, #d9d4c8 60%, #f6b74a 100%);
  }
</style>
</head>
<body>
<main class="flyer">
  <svg class="shapes" width="818" height="1200" viewBox="0 0 818 1200" aria-hidden="true">
    <path d="M818 0 V320 H560 C470 320 430 280 430 200 V120 C430 40 470 0 540 0 Z" fill="var(--orange)"/>
    <path d="M0 800 H330 C380 800 410 830 410 880 V1200 H0 Z" fill="var(--white)"/>
    <path d="M410 800 H818 V1200 H410 Z" fill="var(--orange)"/>
    <path d="M410 800 H818 V830 C700 815 560 815 410 860 Z" fill="var(--orange-light)" opacity="0.5"/>
  </svg>

  <div class="brand">
    <span class="brand-name">Nevrisa</span>
  </div>

  <div class="hero-photo" role="img" aria-label="Fotografie ruky dotýkající se světelných ikon na dotykové obrazovce"></div>

  <section class="intro">
    <h2 class="intro-title">Úvodní představení produktu</h2>
    <p class="intro-text">Program slouží k účetní a operativní evidenci majetku, k evidenci účetních a daňových odpisů a také k evidenci leasingů. Agendu lze zpracovávat i pro více organizací. Měsíční zpracování probíhá ve třech krocích. Nejprve se provedou změny do evidence, dále lze provést automatické zaúčtování majetku a období se uzavře měsíční uzávěrkou, která provede archivaci, posun období a výpočet odpisů. Měsíční uzávěrka za dvanáctý měsíc provede současně roční uzávěrku.</p>
  </section>

  <section class="features">
    <h2 class="features-title">Klíčové vlastnosti produktu</h2>
    <ul class="features-list">
      <li>Přehledné a jednotné pracovní prostředí</li>
      <li>Informace dostupné na minimální počet kliknutí</li>
      <li>Možnost nasazení v různých prostředích</li>
      <li>Nezávislost na operačním systému</li>
      <li>Tisk do PDF souborů s možností využití editovatelných šablon</li>
      <li>Možnost ukládání rozdělané práce</li>
      <li>Úplný převod dat z předchozí verze</li>
    </ul>
  </section>
  <p class="website">www.nevrisa-soft.cz</p>

  <div class="module-band"><span class="module-name">module name</span></div>
  <div class="module-icon" role="img" aria-label="Ikona modulu: kroužkový blok s písmenem A a tužkou"></div>
</main>
</body>
</html>
```